Franchise Power Point

Looking to add a strong design element to a very basic power point presentation about how to find the ideal franchise match. My website is www.brightpathventuring.com and www.vendalink/TKowalczyk

```html
<!DOCTYPE html>
<html lang="en">
<head>
<meta charset="utf-8">
<title>Smart Franchise Decisions – Slide Deck</title>
<link href="https://fonts.googleapis.com/css2?family=Playfair+Display:wght@600;700&family=Montserrat:wght@400;500;600;700;800&display=swap" rel="stylesheet">
<style>
:root{
  --navy:#14304a;
  --navy-deep:#0f2a43;
  --navy-mid:#1d4466;
  --yellow:#fdb813;
  --gold:#f3a200;
  --gold-deep:#d89a00;
  --panel-grey:#dfe3e8;
  --panel-cream:#fff6dc;
  --page:#e4e4e4;
  --white:#ffffff;
  --ink:#14304a;
}
*{box-sizing:border-box;margin:0;padding:0}
html,body{width:749px;height:1200px;overflow:hidden;background:var(--page)}
body{position:relative;font-family:'Montserrat',sans-serif;color:var(--ink)}
.slide{position:absolute;width:258px;height:145px;overflow:hidden;background:var(--white)}
.col-l{left:109px}.col-r{left:384px}
.row1{top:36px}.row2{top:196px}.row3{top:356px}.row4{top:516px}.row5{top:676px}.row6{top:836px}.row7{top:996px}
.slide svg.bg{position:absolute;left:0;top:0;width:258px;height:145px}
.dark{background:var(--navy)}
.serif{font-family:'Playfair Display',serif;font-weight:700}
.abs{position:absolute}
.brand{position:absolute;color:var(--white);font-family:'Playfair Display',serif;font-weight:700;font-size:7px;line-height:1;white-space:nowrap}
.brand .dot{display:inline-block;width:4px;height:4px;border-radius:50%;background:var(--yellow);margin-left:2px;vertical-align:middle}
.brand small{display:block;font-family:'Montserrat',sans-serif;font-weight:400;font-size:2px;margin-top:1.5px;opacity:.8}
.tagline{position:absolute;right:12px;bottom:3px;font-family:'Playfair Display',serif;font-size:3.2px;color:var(--navy-deep);font-weight:600;white-space:nowrap}
.tagline.light{color:var(--white)}
.hero-title{position:absolute;left:13px;color:var(--white);font-size:12.5px;line-height:1.08;white-space:nowrap}
.section-title{position:absolute;left:13px;color:var(--yellow);font-size:10.5px;line-height:1.1;white-space:nowrap}
.photo{position:absolute}
.foot-brand{position:absolute;left:13px;bottom:4px;font-family:'Playfair Display',serif;font-weight:700;font-size:3px;color:var(--white)}
.foot-tag{position:absolute;left:35px;bottom:4px;font-family:'Playfair Display',serif;font-size:2.6px;color:var(--white);white-space:nowrap}
.page-no{position:absolute;right:13px;bottom:3px;font-size:2px;color:var(--white)}
.slide-heading{position:absolute;left:13px;top:14px;font-family:'Playfair Display',serif;font-weight:700;font-size:8.4px;color:var(--ink);white-space:nowrap}
.step-box{position:absolute;top:47px;width:54px;height:72px;border:1px solid var(--navy);text-align:center;font-size:5.2px;line-height:1.22;padding:18px 3px 0}
.step-icon{position:absolute;top:-10px;left:17px;width:20px;height:20px;border-radius:50%;background:var(--yellow)}
.step-icon svg{width:20px;height:20px}
.panel{position:absolute;left:89px;top:13px;right:0;height:108px;padding:6px 0 0 13px}
.panel.grey{background:var(--panel-grey);border-left:2px solid var(--navy)}
.panel.cream{background:var(--panel-cream);border-left:2px solid var(--yellow)}
.panel ul{list-style:none}
.panel li{font-size:4.8px;line-height:9px;position:relative;white-space:nowrap}
.panel li::before{content:"";position:absolute;left:-5px;top:4px;width:1.2px;height:1.2px;border-radius:50%;background:var(--navy)}
.panel.cream li::before{background:var(--yellow)}
.side-title{position:absolute;left:13px;font-family:'Playfair Display',serif;font-weight:700;font-size:8.4px;line-height:1.08;color:var(--ink);white-space:nowrap}
.block{position:absolute;left:0;top:31px;width:148px;height:82px;background:var(--navy);color:var(--white)}
.block::after{content:"";position:absolute;right:-4px;top:0;width:4px;height:100%;background:var(--yellow)}
.brain{text-align:center;font-weight:800;font-size:11px;line-height:1;padding-top:15px}
.brain .vs{display:block;color:var(--yellow);font-size:8px;margin:9px 0 8px}
.fear-text{font-weight:800;font-size:12px;line-height:1.15;padding:25px 0 0 15px}
.donut-label{position:absolute;font-size:5.3px;font-weight:700;line-height:1.05;color:#111;white-space:nowrap}
.donut-label.end{text-align:right}
.contact{position:absolute;left:120px;font-size:5.4px;color:var(--navy-deep)}
.contact .ico{position:absolute;left:0;top:-3.5px;width:10px;height:10px;border-radius:50%;background:var(--white)}
.contact .ico svg{width:10px;height:10px}
.contact span{position:absolute;left:15px;top:0;white-space:nowrap}
.contact span.link{text-decoration:underline}
.contact .rule{position:absolute;left:15px;top:11px;width:6px;height:.5px;background:var(--navy-deep)}
.caption{position:absolute;left:0;width:749px;top:1160px;text-align:center;font-size:11px;line-height:9px;color:#111}
</style>
</head>
<body>

<!-- Slide 1: title with photo -->
<section class="slide dark col-l row1">
  <div class="photo" role="img" aria-label="Photo of a businessman in a suit looking upward against blurred city buildings" style="left:90px;top:0;width:168px;height:135px;background:linear-gradient(90deg,var(--navy) 0%,#2b4c70 45%,#4d6f93 75%,#c99a3a 100%)"></div>
  <svg class="bg" viewBox="0 0 258 145"><polygon points="0,139 258,131 258,145 0,145" fill="var(--yellow)"/></svg>
  <div class="brand" style="left:14px;top:56px">Vendalink<span class="dot"></span><small>Guiding Owners Toward Their Goals</small></div>
  <h1 class="hero-title serif" style="top:77px">Smart Franchise Decisions<br>Using Logic and Intuition</h1>
  <div class="tagline">Guiding Owners Toward Their Goals</div>
</section>

<!-- Slide 2: plain title -->
<section class="slide dark col-r row1">
  <svg class="bg" viewBox="0 0 258 145"><polygon points="0,139 258,131 258,145 0,145" fill="var(--yellow)"/></svg>
  <div class="brand" style="left:14px;top:38px">Vendalink<span class="dot"></span><small>Guiding Owners Toward Their Goals</small></div>
  <h1 class="hero-title serif" style="top:59px">Smart Franchise Decisions<br>Using Logic and Intuition</h1>
  <div class="tagline">Guiding Owners Toward Their Goals</div>
</section>

<!-- Slide 3: section -->
<section class="slide dark col-l row2">
  <svg class="bg" viewBox="0 0 258 145">
    <polygon points="0,95 258,102 258,145 0,145" fill="var(--navy-mid)"/>
    <polygon points="0,97 82,103 0,112" fill="var(--yellow)"/>
  </svg>
  <h2 class="section-title serif" style="top:34px">Do not let your Entrepreneurial Dream<br>turn a Technicians Nightmare</h2>
  <div class="brand" style="left:13px;top:126px">Vendalink<span class="dot"></span><small>Guiding Owners Toward Their Goals</small></div>
  <div class="tagline light">Guiding Owners Toward Their Goals</div>
</section>

<!-- Slide 4: section -->
<section class="slide dark col-r row2">
  <svg class="bg" viewBox="0 0 258 145">
    <polygon points="0,95 258,102 258,145 0,145" fill="var(--navy-mid)"/>
    <polygon points="0,97 82,103 0,112" fill="var(--yellow)"/>
  </svg>
  <h2 class="section-title serif" style="top:45px">Use the Educated Approach</h2>
  <div class="brand" style="left:13px;top:126px">Vendalink<span class="dot"></span><small>Guiding Owners Toward Their Goals</small></div>
  <div class="tagline light">Guiding Owners Toward Their Goals</div>
</section>

<!-- Slide 5: educated approach steps -->
<section class="slide col-l row3">
  <h3 class="slide-heading">What is the Educated Approach?</h3>
  <div class="step-box" style="left:12px"><div class="step-icon"><svg viewBox="0 0 20 20"><circle cx="10" cy="10" r="5" fill="none" stroke="var(--navy)" stroke-width=".9"/><circle cx="10" cy="10" r="2.3" fill="none" stroke="var(--navy)" stroke-width=".9"/><line x1="10" y1="10" x2="15" y2="5" stroke="var(--navy)" stroke-width=".9"/></svg></div>First Define<br>the Ideal Fit</div>
  <div class="step-box" style="left:72px"><div class="step-icon"><svg viewBox="0 0 20 20"><circle cx="10" cy="10" r="5" fill="none" stroke="var(--navy)" stroke-width=".9"/><line x1="6" y1="6" x2="14" y2="14" stroke="var(--navy)" stroke-width=".9"/><line x1="14" y1="6" x2="6" y2="14" stroke="var(--navy)" stroke-width=".9"/></svg></div>Focus on<br>options that fit<br>your strengths</div>
  <div class="step-box" style="left:131px"><div class="step-icon"><svg viewBox="0 0 20 20"><polygon points="5,9 10,5 15,9" fill="none" stroke="var(--navy)" stroke-width=".9"/><rect x="6" y="9" width="8" height="6" fill="none" stroke="var(--navy)" stroke-width=".9"/></svg></div>Focus on<br>options that will<br>meet your<br>lifestyle and<br>financial<br>goals while<br>reducing risk</div>
  <div class="step-box" style="left:191px"><div class="step-icon"><svg viewBox="0 0 20 20"><circle cx="9" cy="9" r="3.5" fill="none" stroke="var(--navy)" stroke-width=".9"/><line x1="11.5" y1="11.5" x2="15" y2="15" stroke="var(--navy)" stroke-width="1.2"/></svg></div>Put yourself at<br>the center of<br>the search</div>
  <svg class="bg" viewBox="0 0 258 145"><polygon points="0,136 258,130 258,145 0,145" fill="var(--navy)"/><polygon points="150,134 258,130 258,133" fill="var(--yellow)"/></svg>
  <div class="foot-brand">Vendalink</div><div class="foot-tag">Guiding Owners Toward Their Goals</div><div class="page-no">5</div>
</section>

<!-- Slide 6: key questions -->
<section class="slide col-r row3">
  <svg class="abs" style="left:12px;top:29px" width="22" height="22" viewBox="0 0 22 22"><circle cx="11" cy="10" r="7" fill="none" stroke="var(--navy)" stroke-width=".8"/><circle cx="11" cy="10" r="3" fill="none" stroke="var(--navy)" stroke-width=".8"/><rect x="8" y="17" width="6" height="3" fill="none" stroke="var(--navy)" stroke-width=".8"/></svg>
  <h3 class="side-title" style="top:60px">Sample Key<br>Questions<br>for the Educated<br>Approach</h3>
  <div class="panel grey"><ul>
    <li>Proper investment level</li><li>Skill set and background / personality matching</li><li>Return goals – short, mid and long term</li><li>Employee profile: numbers &amp; backgrounds</li><li>Sales, marketing and advertising</li><li>Concerns around the economy</li><li>Need vs want</li><li>Residual / Repeat / Reoccurring</li><li>Status</li><li>B2B vs B2C</li><li>Full time vs part time vs. managed services</li>
  </ul></div>
  <svg class="bg" viewBox="0 0 258 145"><polygon points="0,136 258,130 258,145 0,145" fill="var(--navy)"/><polygon points="150,134 258,130 258,133" fill="var(--yellow)"/></svg>
  <div class="foot-brand">Vendalink</div><div class="foot-tag">Guiding Owners Toward Their Goals</div><div class="page-no">6</div>
</section>

<!-- Slide 7: research method -->
<section class="slide col-l row4">
  <svg class="abs" style="left:13px;top:40px" width="24" height="22" viewBox="0 0 24 22"><rect x="8" y="3" width="14" height="17" fill="none" stroke="var(--navy)" stroke-width=".8"/><circle cx="7" cy="8" r="5" fill="none" stroke="var(--navy)" stroke-width=".8"/><line x1="11" y1="16" x2="11" y2="12" stroke="var(--navy)" stroke-width="1"/><line x1="14" y1="16" x2="14" y2="10" stroke="var(--navy)" stroke-width="1"/><line x1="17" y1="16" x2="17" y2="13" stroke="var(--navy)" stroke-width="1"/></svg>
  <h3 class="side-title" style="top:68px">The Research<br>Method</h3>
  <div class="panel cream"><ul>
    <li>Define your ideal match</li><li>Establish contact with target franchisor</li><li>Work through their standard process</li><li>Review FDD</li><li>Validate with franchisees</li><li>Explore financing options</li><li>Discuss territory</li><li>Put together cash flow projections</li><li>Attend Discovery Day</li><li>Make a decision</li>
  </ul></div>
  <svg class="bg" viewBox="0 0 258 145"><polygon points="0,136 258,130 258,145 0,145" fill="var(--navy)"/><polygon points="150,134 258,130 258,133" fill="var(--yellow)"/></svg>
  <div class="foot-brand">Vendalink</div><div class="foot-tag">Guiding Owners Toward Their Goals</div><div class="page-no">7</div>
</section>

<!-- Slide 8: decision making -->
<section class="slide col-r row4">
  <div class="photo" role="img" aria-label="Photo of a weathered stone statue of a seated thinking figure with a gull perched on top" style="left:148px;top:0;width:110px;height:136px;background:linear-gradient(160deg,#6b4a2a 0%,#8a6a48 40%,#b7ab9c 70%,#5a4330 100%)"></div>
  <h3 class="slide-heading">Decision Making</h3>
  <div class="block brain">Right Brain<span class="vs">vs.</span>Left Brain</div>
  <svg class="bg" viewBox="0 0 258 145"><polygon points="0,136 258,130 258,145 0,145" fill="var(--navy)"/><polygon points="150,134 258,130 258,133" fill="var(--yellow)"/></svg>
  <div class="foot-brand">Vendalink</div><div class="foot-tag">Guiding Owners Toward Their Goals</div><div class="page-no">8</div>
</section>

<!-- Slide 9: fear -->
<section class="slide col-l row5">
  <div class="photo" role="img" aria-label="Photo of an ancient skeleton lying in reddish earth" style="left:148px;top:0;width:110px;height:136px;background:linear-gradient(150deg,#3a1e10 0%,#8a4a22 45%,#b9743e 65%,#4a2614 100%)"></div>
  <h3 class="slide-heading">Fear</h3>
  <div class="block fear-text">The human spirit<br>resist’s change</div>
  <svg class="bg" viewBox="0 0 258 145"><polygon points="0,136 258,130 258,145 0,145" fill="var(--navy)"/><polygon points="150,134 258,130 258,133" fill="var(--yellow)"/></svg>
  <div class="foot-brand">Vendalink</div><div class="foot-tag">Guiding Owners Toward Their Goals</div><div class="page-no">9</div>
</section>

<!-- Slide 10: dam or river -->
<section class="slide col-r row5">
  <div class="photo" role="img" aria-label="Aerial photo of a turquoise river winding between rocky canyon walls below a dam" style="left:96px;top:0;width:162px;height:136px;background:linear-gradient(135deg,#8c8878 0%,#5f7166 35%,#2f6570 55%,#6f7a6c 80%,#b5b0a2 100%)"></div>
  <h3 class="side-title" style="top:47px">Are you<br>the dam or<br>are you<br>the River?</h3>
  <svg class="bg" viewBox="0 0 258 145"><polygon points="0,136 258,130 258,145 0,145" fill="var(--navy)"/><polygon points="150,134 258,130 258,133" fill="var(--yellow)"/></svg>
  <div class="foot-brand">Vendalink</div><div class="foot-tag">Guiding Owners Toward Their Goals</div><div class="page-no">10</div>
</section>

<!-- Slide 11: booth offer -->
<section class="slide col-l row6">
  <div class="abs" style="left:96px;top:0;width:162px;height:136px;background:#f1f1f1"></div>
  <div class="photo" role="img" aria-label="Cover of the book The Owner's Field Guide, second edition, with an apple illustration" style="left:125px;top:6px;width:103px;height:123px;background:linear-gradient(180deg,#2b5f7d 0%,#2b5f7d 38%,#f3f3f1 38%,#e8ece6 92%,#2b5f7d 92%)"></div>
  <h3 class="side-title" style="top:33px">Stop by my Booth,<br>Ask Me ANY<br>Question and<br>Receive a Free<br>Copy of The<br>Owner's Field<br>Guide</h3>
  <svg class="bg" viewBox="0 0 258 145"><polygon points="0,136 258,130 258,145 0,145" fill="var(--navy)"/><polygon points="150,134 258,130 258,133" fill="var(--yellow)"/></svg>
  <div class="foot-brand">Vendalink</div><div class="foot-tag">Guiding Owners Toward Their Goals</div><div class="page-no">11</div>
</section>

<!-- Slide 12: top dozen navy -->
<section class="slide col-r row6">
  <h3 class="slide-heading" style="top:17px">My Top Dozen for 2024</h3>
  <svg class="bg" viewBox="0 0 258 145">
    <circle cx="129" cy="78" r="33.5" fill="none" stroke="var(--navy)" stroke-width="17"/>
    <g stroke="var(--white)" stroke-width="1.4">
      <line x1="129" y1="34" x2="129" y2="122"/>
      <line x1="90.9" y1="56" x2="167.1" y2="100"/>
      <line x1="90.9" y1="100" x2="167.1" y2="56"/>
    </g>
    <circle cx="129" cy="78" r="25" fill="var(--white)"/>
    <g fill="none" stroke="var(--white)" stroke-width=".6">
      <circle cx="112" cy="61" r="3"/><circle cx="145" cy="61" r="3"/><circle cx="100" cy="78" r="3"/><circle cx="158" cy="78" r="3"/><circle cx="112" cy="95" r="3"/><circle cx="145" cy="95" r="3"/>
    </g>
    <polygon points="0,136 258,130 258,145 0,145" fill="var(--navy)"/><polygon points="150,134 258,130 258,133" fill="var(--yellow)"/>
  </svg>
  <div class="donut-label end" style="right:166px;top:42px">Pet Options</div>
  <div class="donut-label" style="left:166px;top:42px">Seniors and Children</div>
  <div class="donut-label end" style="right:178px;top:77px">Real Estate Options</div>
  <div class="donut-label" style="left:178px;top:77px">Health and Wellness</div>
  <div class="donut-label end" style="right:166px;top:113px">Mental Health</div>
  <div class="donut-label" style="left:166px;top:109px">Owner Operator<br>to Area Developer</div>
  <div class="foot-brand">Vendalink</div><div class="foot-tag">Guiding Owners Toward Their Goals</div><div class="page-no">12</div>
</section>

<!-- Slide 13: top dozen yellow -->
<section class="slide col-l row7">
  <h3 class="slide-heading" style="top:17px">My Top Dozen for 2024</h3>
  <svg class="bg" viewBox="0 0 258 145">
    <circle cx="128" cy="78" r="33.5" fill="none" stroke="var(--yellow)" stroke-width="17"/>
    <path d="M128 44.5 A33.5 33.5 0 0 0 99 61.25" fill="none" stroke="var(--gold-deep)" stroke-width="17"/>
    <path d="M157 61.25 A33.5 33.5 0 0 1 157 94.75" fill="none" stroke="var(--gold-deep)" stroke-width="17"/>
    <path d="M99 94.75 A33.5 33.5 0 0 0 128 111.5" fill="none" stroke="var(--gold-deep)" stroke-width="17"/>
    <g stroke="var(--white)" stroke-width="1.4">
      <line x1="128" y1="34" x2="128" y2="122"/>
      <line x1="89.9" y1="56" x2="166.1" y2="100"/>
      <line x1="89.9" y1="100" x2="166.1" y2="56"/>
    </g>
    <circle cx="128" cy="78" r="25" fill="var(--white)"/>
    <g fill="none" stroke="var(--navy)" stroke-width=".6">
      <circle cx="111" cy="61" r="3"/><circle cx="144" cy="61" r="3"/><rect x="96" y="76" width="7" height="4"/><circle cx="157" cy="78" r="3"/><polyline points="108,97 111,93 114,97"/><rect x="140" y="93" width="8" height="4"/>
    </g>
    <polygon points="0,136 258,130 258,145 0,145" fill="var(--navy)"/><polygon points="150,134 258,130 258,133" fill="var(--yellow)"/>
  </svg>
  <div class="donut-label end" style="right:166px;top:42px">Emergency Restoration</div>
  <div class="donut-label" style="left:166px;top:42px">Rental Options</div>
  <div class="donut-label end" style="right:178px;top:77px">Low Status Options</div>
  <div class="donut-label" style="left:178px;top:77px">Clothing Recycling</div>
  <div class="donut-label end" style="right:166px;top:113px">Home Services</div>
  <div class="donut-label" style="left:166px;top:109px">Food Trucks /<br>Restaurants</div>
  <div class="foot-brand">Vendalink</div><div class="foot-tag">Guiding Owners Toward Their Goals</div><div class="page-no">13</div>
</section>

<!-- Slide 14: closing contact -->
<section class="slide dark col-r row7">
  <svg class="bg" viewBox="0 0 258 145">
    <defs><linearGradient id="closeGrad" x1="0" y1="0" x2="1" y2="1"><stop offset="0" stop-color="var(--yellow)"/><stop offset="1" stop-color="var(--gold)"/></linearGradient></defs>
    <polygon points="129,0 258,0 258,145 46,145" fill="url(#closeGrad)"/>
  </svg>
  <div class="brand" style="left:14px;top:18px">Vendalink<span class="dot"></span><small>Guiding Owners Toward Their Goals</small></div>
  <h2 class="serif abs" style="left:13px;top:64px;font-size:12px;color:var(--white)">Courtesy of</h2>
  <div class="contact" style="top:43px"><div class="ico"><svg viewBox="0 0 10 10"><path d="M5 2.2a1.6 1.6 0 0 1 1.6 1.6C6.6 5 5 7.3 5 7.3S3.4 5 3.4 3.8A1.6 1.6 0 0 1 5 2.2z" fill="none" stroke="var(--navy)" stroke-width=".5"/></svg></div><span>Tess Kowalczyk</span><div class="rule"></div></div>
  <div class="contact" style="top:64px"><div class="ico"><svg viewBox="0 0 10 10"><path d="M3 2.5l1.2 1.6-.6.8c.4.9 1 1.5 1.9 1.9l.8-.6 1.6 1.2-.7 1C5 8 2.2 5.2 2.4 3.2z" fill="none" stroke="var(--navy)" stroke-width=".5"/></svg></div><span>555.014.2287</span><div class="rule"></div></div>
  <div class="contact" style="top:85px"><div class="ico"><svg viewBox="0 0 10 10"><rect x="2.5" y="3.2" width="5" height="3.6" fill="none" stroke="var(--navy)" stroke-width=".5"/><polyline points="2.5,3.2 5,5.2 7.5,3.2" fill="none" stroke="var(--navy)" stroke-width=".5"/></svg></div><span class="link">tkowalczyk@vendalink.com</span><div class="rule"></div></div>
  <div class="contact" style="top:106px"><div class="ico"><svg viewBox="0 0 10 10"><circle cx="5" cy="5" r="2.6" fill="none" stroke="var(--navy)" stroke-width=".5"/><line x1="2.4" y1="5" x2="7.6" y2="5" stroke="var(--navy)" stroke-width=".4"/><ellipse cx="5" cy="5" rx="1.1" ry="2.6" fill="none" stroke="var(--navy)" stroke-width=".4"/></svg></div><span class="link">http://www.brightpathventuring.com</span></div>
  <div class="tagline">Guiding Owners Toward Their Goals</div>
</section>

<p class="caption">and all slide of presentation have done<br>(all slide is editable slide)</p>

</body>
</html>
```